Website Design for Freeze-Dried Food Manufacturing Company (Pet Food & Agri-Food)

We are looking for a high-level web designer to create a clean, modern, premium website design for Brindle, a freeze-dried food manufacturing company operating in both the pet food and agri-food space.
This is not a basic website build β we are looking for a designer who understands brand positioning, layout, and user flow, not just visuals.
π― Project Objective
Design a website that:
Clearly communicates our capabilities and value proposition
Feels premium, credible, and product-driven
Guides users through a simple, intuitive journey
Clean and Crips
A critical requirement is clearly separating:
π Pet Food
π Agri-Food
These must feel like two distinct pathways within the same brand experience.
We have attached detailed documents outlining structure, layout, and messaging. These should be followed closely.
π What Success Looks Like
A high-impact homepage with strong visual hierarchy
Clear entry points into Pet Food and Agri-Food
Clean, intentional layout (not cluttered or template-like)
Thoughtful spacing, typography, and flow
A design that feels considered and elevated, not generic
π¨ Design Direction
We are aiming for a:
Minimal, premium aesthetic
Warm, natural color palette (creams, browns, muted tones)
Ingredient and product-focused visuals
Avoid:
Overly corporate / industrial styles
Generic SaaS-style layouts
Busy or over-designed interfaces
End Goal
A website that immediately communicates:
Who we are
What we do
Why weβre different
In a way that feels premium, clear, and easy to navigate.
Link to current website: https://brindleharvest.example/
https://brindlelabs.example/wp-admin/

```html
<!DOCTYPE html>
<html lang="en">
<head>
<meta charset="utf-8">
<title>Brindle — Freeze Drying &amp; Food Manufacturing</title>
<link href="https://fonts.googleapis.com/css2?family=Lexend:wght@400;500;600;700;800&family=DM+Sans:wght@400;500;700&display=swap" rel="stylesheet">
<style>
:root{
  --rust:#b8683a;
  --rust-dark:#8f4b25;
  --cream:#f8f1e6;
  --cream-2:#f3e7d6;
  --tan:#d59c68;
  --brown:#4a2b1c;
  --ink:#231f1d;
  --gold:#d8a060;
  --muted:#7a6a5d;
  --line:#d9c4ad;
  --white:#ffffff;
  --ghost:#efe4d4;
}
*{box-sizing:border-box;margin:0;padding:0}
html,body{width:1200px;height:4216px;overflow:hidden}
body{font-family:"DM Sans",sans-serif;color:var(--ink);background:var(--cream);position:relative}
h1,h2,h3,.display{font-family:"Lexend",sans-serif}
section,header,footer{position:relative;width:1200px;overflow:hidden}
.abs{position:absolute}
.ph{position:absolute}
.btn{display:inline-flex;align-items:center;gap:10px;border-radius:30px;font:600 12px "Lexend",sans-serif;color:var(--white);padding:9px 10px 9px 18px;border:2px solid rgba(255,255,255,.35);white-space:nowrap}
.btn .arr{width:20px;height:20px;border:1.5px solid currentColor;border-radius:50%;display:grid;place-items:center}
.btn-rust{background:var(--rust)}
.btn-brown{background:var(--brown)}

/* top bar + nav */
.topbar{height:28px;background:var(--rust);color:var(--white);font-size:12px;text-align:center;line-height:28px}
.nav{height:80px;background:var(--cream);display:flex;align-items:center;padding:0 110px}
.logo{font:800 20px "Lexend",sans-serif;color:var(--brown);letter-spacing:.5px;width:125px}
.menu{display:flex;gap:30px;font:500 12px "Lexend",sans-serif;color:var(--ink)}
.menu .on{color:var(--rust)}
.nav-right{margin-left:auto;display:flex;align-items:center;gap:14px;font:600 15px "Lexend",sans-serif}
.ic{width:22px;height:22px;border:1.5px solid var(--ink);border-radius:50%;display:grid;place-items:center}
.socials{display:flex;gap:6px}

/* hero */
.hero{height:620px;background:var(--cream)}
.hero-bg{left:0;top:0;width:1200px;height:570px;background:linear-gradient(100deg,#2c221c 0%,#4a3c32 45%,#5c4d42 70%,#3a2f28 100%)}
.hero-edge{left:0;top:560px}
.hero-copy{left:110px;top:110px;color:var(--white)}
.eyebrow{font-size:12px;color:var(--gold);display:flex;align-items:center;gap:8px}
.eyebrow::after{content:"";width:34px;height:1px;background:var(--gold)}
.hero h1{font-size:46px;line-height:56px;font-weight:800;letter-spacing:1px;margin-top:14px}
.hero h1 .gold{color:var(--gold)}
.hero p{font-size:14px;line-height:20px;margin:14px 0 30px;width:500px;color:#f1e6da}
.hero-dog{left:540px;top:250px;width:260px;height:350px;border-radius:120px 120px 20px 20px;background:radial-gradient(circle at 50% 40%,#c98a52,#8a5530 70%,transparent 71%)}
.hero-bowl{left:700px;top:420px;width:210px;height:150px;border-radius:20px 20px 100px 100px;background:linear-gradient(#9a5629,#f4efea 55%)}
.hero-veg{left:820px;top:180px;width:240px;height:240px;border-radius:50%;border:6px solid var(--white);background:radial-gradient(circle at 35% 35%,#e0c23a,#c8362b 40%,#4f8a2a 75%)}

/* features */
.features{height:140px;display:flex;justify-content:center;gap:60px;align-items:center}
.feat{display:flex;align-items:center;gap:14px;font:500 14px "Lexend",sans-serif}
.feat .circ{width:54px;height:54px;border-radius:50%;border:1.5px solid var(--line);background:var(--white);display:grid;place-items:center}

/* pathways */
.paths{height:560px}
.path h2{font-size:30px;font-weight:800;letter-spacing:1px;color:var(--ink);margin:10px 0 10px}
.path p{font-size:12px;line-height:17px;color:var(--muted);width:210px;margin-bottom:18px}
.path-pet{left:140px;top:20px}
.path-agri{left:875px;top:20px}
.halo{left:350px;top:20px;width:500px;height:500px;border-radius:50%;background:var(--cream-2)}
.split{left:390px;top:60px;width:420px;height:420px;border-radius:50%;overflow:hidden;border:8px solid #f1dfc8}
.split .l{position:absolute;left:0;top:0;width:50%;height:100%;background:linear-gradient(160deg,#d76a4d,#c9a24c 50%,#8e3a4a)}
.split .r{position:absolute;right:0;top:0;width:50%;height:100%;background:linear-gradient(200deg,#6c9b3a,#3f7b2b 50%,#6a3f25)}
.bag{width:110px;height:140px;border-radius:10px;background:linear-gradient(#eee8e2,#d5c7bb)}
.bag-pet{left:150px;top:400px}
.bag-agri{left:905px;top:400px;background:linear-gradient(#f4e9c9,#9ec26b 60%,#e59a46)}

/* dedicated */
.dedicated{height:200px;background:var(--tan);color:var(--white);text-align:center;padding-top:62px}
.dedicated h2{font-size:30px;font-weight:800;letter-spacing:1px}
.dedicated p{font-size:14px;line-height:19px;margin-top:10px}

/* loop */
.loop{height:480px;text-align:center;padding-top:70px}
.sec-title{font-size:30px;font-weight:800;letter-spacing:1px}
.sec-sub{font-size:12px;color:var(--muted);margin-top:8px}
.steps{position:relative;display:flex;justify-content:space-between;width:920px;margin:60px auto 0}
.steps::before{content:"";position:absolute;left:40px;right:40px;top:35px;border-top:1.5px dashed var(--line)}
.step{position:relative;width:110px;text-align:center}
.step .circ{width:70px;height:70px;margin:0 auto;border-radius:50%;background:var(--white);border:1.5px solid var(--line);display:grid;place-items:center;box-shadow:0 0 0 6px var(--cream)}
.step .num{font:500 14px "Lexend",sans-serif;color:var(--gold);margin-top:20px}
.step .lbl{font:500 15px "Lexend",sans-serif;margin-top:10px}

/* capabilities */
.caps{height:640px;text-align:center;padding-top:20px}
.cards{display:flex;justify-content:center;gap:50px;margin-top:40px}
.card{width:280px;height:340px;background:#fbe6c8;border-radius:12px;padding:10px;text-align:left;position:relative}
.card .img{width:260px;height:240px;border-radius:8px}
.card h3{font-size:14px;font-weight:500;margin:14px 6px 4px}
.card p{font-size:11px;line-height:14px;color:var(--muted);margin:0 6px;width:180px}
.card .go{position:absolute;right:20px;bottom:26px;width:22px;height:22px;border:1.5px solid var(--ink);border-radius:50%;display:grid;place-items:center}

/* why */
.why{height:720px}
.why h2{left:145px;top:30px;font-size:32px;font-weight:800;letter-spacing:1px}
.ghost{left:490px;top:470px;font:800 120px "Lexend",sans-serif;color:var(--ghost);letter-spacing:6px;line-height:1}
.why-person{left:90px;top:110px;width:320px;height:610px;border-radius:160px 160px 0 0;background:linear-gradient(#3a2a22 0%,#c79c7a 35%,#4e4540 70%,#3d3732)}
.why-halo{left:400px;top:10px;width:400px;height:400px;border-radius:50%;background:var(--cream-2)}
.why-circle{left:420px;top:30px;width:360px;height:360px;border-radius:50%;background:linear-gradient(160deg,#5f6468,#d4c52c 45%,#444a4f)}
.why-item{display:flex;align-items:center;gap:16px;font:500 15px "Lexend",sans-serif}
.why-item .circ{width:56px;height:56px;border-radius:50%;background:var(--brown);color:var(--white);display:grid;place-items:center;box-shadow:0 0 0 6px var(--cream-2)}
.dot{width:14px;height:14px;border-radius:50%;border:3px solid var(--gold);background:var(--white)}

/* cta */
.cta{height:360px;background:var(--rust);color:var(--white)}
.cta h2{left:180px;top:80px;font-size:32px;line-height:38px;font-weight:800;letter-spacing:1px}
.cta p{left:180px;top:170px;font-size:13px;line-height:18px;width:420px}
.cta .btn{left:180px;top:235px;position:absolute;border-color:rgba(255,255,255,.6)}
.cta-halo{left:780px;top:60px;width:300px;height:300px;border-radius:50%;background:#c8784a}
.cta-bag1{left:700px;top:100px;width:160px;height:190px;border-radius:12px;background:linear-gradient(#f1ebe4,#cdbfb1)}
.cta-bag2{left:850px;top:70px;width:160px;height:210px;border-radius:12px;background:linear-gradient(#f4e9c9,#9ec26b 55%,#e59a46)}

/* footer */
.foot{height:388px;background:var(--ink);color:var(--white)}
.cols{display:flex;padding:90px 110px 0}
.col{font-size:11px;color:#cfc6bd;line-height:16px}
.col h4{font:600 12px "Lexend",sans-serif;color:var(--white);letter-spacing:.5px;margin-bottom:18px}
.col ul{list-style:none}
.col li{margin-bottom:10px;display:flex;align-items:center;gap:8px}
.col li span.txt{min-width:0;overflow-wrap:anywhere}
.sic{width:20px;height:20px;border-radius:50%;border:1.5px solid #cfc6bd;flex:none}
.flogo{font:800 20px "Lexend",sans-serif;color:var(--white)}
.email{width:160px;height:32px;border:1px solid #6a625c;border-radius:20px;font-size:10px;padding:0 14px;line-height:30px;color:#aaa}
.copyright{position:absolute;left:0;right:0;bottom:24px;text-align:center;font-size:10px;color:#aaa}
.vline{position:absolute;top:80px;width:1px;height:190px;background:#3c3632}
</style>
</head>
<body>

<header>
  <div class="topbar">Agrifood, life-science &amp; pharmaceutical processing &amp; storage specialists</div>
  <nav class="nav">
    <div class="logo">BRINDLE</div>
    <div class="menu"><span class="on">Home</span><span>Pet Food</span><span>Agri-Food</span><span>Capabilities</span><span>Capabilities</span></div>
    <div class="nav-right">
      <span style="display:flex;align-items:center;gap:6px"><span class="ic"><svg width="11" height="11" viewBox="0 0 24 24" fill="none" stroke="#231f1d" stroke-width="2.4"><path d="M5 3h4l2 5-3 2a12 12 0 0 0 6 6l2-3 5 2v4a2 2 0 0 1-2 2A18 18 0 0 1 3 5a2 2 0 0 1 2-2z"/></svg></span>+1 555 014 2290</span>
      <span class="socials"><span class="ic" aria-label="Photo Feed"></span><span class="ic" aria-label="Updates"></span><span class="ic" aria-label="Network"></span></span>
      <span class="btn btn-brown" style="border-color:#d9c4ad">Contact Us <span class="arr"><svg width="9" height="9" viewBox="0 0 10 10" fill="none" stroke="#fff" stroke-width="1.6"><path d="M2 5h6M5 2l3 3-3 3"/></svg></span></span>
    </div>
  </nav>
</header>

<section class="hero">
  <div class="ph hero-bg" role="img" aria-label="Dim industrial food processing hall with steel tables"></div>
  <svg class="abs hero-edge" width="1200" height="20" viewBox="0 0 1200 20"><path d="M0 0H1200V10Q1190 16 1180 10T1160 10T1140 10T1120 10T1100 10T1080 10T1060 10T1040 10T1020 10T1000 10T980 10T960 10T940 10T920 10T900 10T880 10T860 10T840 10T820 10T800 10T780 10T760 10T740 10T720 10T700 10T680 10T660 10T640 10T620 10T600 10T580 10T560 10T540 10T520 10T500 10T480 10T460 10T440 10T420 10T400 10T380 10T360 10T340 10T320 10T300 10T280 10T260 10T240 10T220 10T200 10T180 10T160 10T140 10T120 10T100 10T80 10T60 10T40 10T20 10T0 10Z" fill="#3a2f28"/></svg>
  <div class="ph hero-veg" role="img" aria-label="Fresh vegetables, peppers and grains in a round frame"></div>
  <div class="ph hero-dog" role="img" aria-label="Young dog sitting beside a food bowl"></div>
  <div class="ph hero-bowl" role="img" aria-label="White bowl filled with dry pet food kibble"></div>
  <div class="abs hero-copy">
    <div class="eyebrow">Nutrition, Frozen in Time</div>
    <h1>INDUSTRIAL FREEZE<br><span class="gold">DRYING &amp; FOOD</span><br>MANUFACTURING</h1>
    <p>A fully integrated, closed-loop system from ingredient sourcing through to production, packaging, and distribution.</p>
    <span class="btn btn-rust">Start a Project <span class="arr"><svg width="9" height="9" viewBox="0 0 10 10" fill="none" stroke="#fff" stroke-width="1.6"><path d="M2 5h6M5 2l3 3-3 3"/></svg></span></span>
  </div>
</section>

<section class="features">
  <div class="feat"><span class="circ"><svg width="24" height="24" viewBox="0 0 24 24" fill="none" stroke="#4a2b1c" stroke-width="1.5"><path d="M3 21V10l5 3V10l5 3V6h5v15z"/></svg></span>OEM Manufacturing</div>
  <div class="feat"><span class="circ"><svg width="24" height="24" viewBox="0 0 24 24" fill="none" stroke="#4a2b1c" stroke-width="1.5"><path d="M4 21V9l8-5 8 5v12M8 21v-8M12 21v-8M16 21v-8"/></svg></span>Freeze-Drying Experts</div>
  <div class="feat"><span class="circ"><svg width="24" height="24" viewBox="0 0 24 24" fill="none" stroke="#4a2b1c" stroke-width="1.5"><circle cx="12" cy="12" r="8"/><path d="M12 7l4 2.5v5L12 17l-4-2.5v-5z"/></svg></span>End-to-End Production</div>
</section>

<section class="paths">
  <div class="ph halo"></div>
  <div class="ph split"><div class="l" role="img" aria-label="Colourful freeze-dried pet treat cubes"></div><div class="r" role="img" aria-label="Freeze-dried green beans and vegetables"></div></div>
  <div class="abs path path-pet">
    <svg width="40" height="32" viewBox="0 0 40 32" fill="none" stroke="#4a2b1c" stroke-width="1.6"><path d="M4 28V14q0-8 16-8t16 8v14z"/><circle cx="15" cy="18" r="2"/><circle cx="25" cy="18" r="2"/></svg>
    <h2>PET FOOD</h2>
    <p>Freeze-dried meals, toppers, and treats designed for quality, consistency, and performance.</p>
    <span class="btn btn-rust" style="border-color:#e6c8a9">Explore Pet Food <span class="arr"><svg width="9" height="9" viewBox="0 0 10 10" fill="none" stroke="#fff" stroke-width="1.6"><path d="M2 5h6M5 2l3 3-3 3"/></svg></span></span>
  </div>
  <div class="abs path path-agri">
    <svg width="40" height="36" viewBox="0 0 40 36" fill="none" stroke="#4a2b1c" stroke-width="1.6"><path d="M6 32C6 14 18 4 36 4 36 22 26 32 6 32zM6 32L24 14"/></svg>
    <h2>AGRI FOOD</h2>
    <p>Ingredient processing and preservation solutions for food and agricultural applications.</p>
    <span class="btn btn-rust" style="border-color:#e6c8a9">Explore Agri Food <span class="arr"><svg width="9" height="9" viewBox="0 0 10 10" fill="none" stroke="#fff" stroke-width="1.6"><path d="M2 5h6M5 2l3 3-3 3"/></svg></span></span>
  </div>
  <div class="ph bag bag-pet" role="img" aria-label="Clear pouch of freeze-dried pet treats"></div>
  <div class="ph bag bag-agri" role="img" aria-label="Clear pouch of freeze-dried mixed vegetables"></div>
</section>

<section class="dedicated">
  <h2>DEDICATED PRODUCTION ENVIRONMENTS</h2>
  <p>Pet food and agri-food production are handled in separate, controlled environments<br>to ensure product integrity and category-specific standards.</p>
</section>

<section class="loop">
  <h2 class="sec-title">A COMPLETE, CLOSED LOOP SYSTEM</h2>
  <p class="sec-sub">We manage every stage in-house, allowing full control over quality, consistency, and speed to market.</p>
  <div class="steps">
    <div class="step"><div class="circ"><svg width="30" height="30" viewBox="0 0 24 24" fill="none" stroke="#4a2b1c" stroke-width="1.3"><path d="M9 18h6M10 21h4M12 3a6 6 0 0 0-4 10.5V16h8v-2.5A6 6 0 0 0 12 3z"/></svg></div><div class="num">01</div><div class="lbl">Concept</div></div>
    <div class="step"><div class="circ"><svg width="30" height="30" viewBox="0 0 24 24" fill="none" stroke="#4a2b1c" stroke-width="1.3"><circle cx="12" cy="12" r="9"/><path d="M12 19V8M12 12l-3-3M12 14l3-3"/></svg></div><div class="num">02</div><div class="lbl">Sourcing</div></div>
    <div class="step"><div class="circ"><svg width="30" height="30" viewBox="0 0 24 24" fill="none" stroke="#4a2b1c" stroke-width="1.3"><path d="M3 20h18M5 20V10h14v10M8 10V6h8v4M9 14h6"/></svg></div><div class="num">03</div><div class="lbl">R&amp;D</div></div>
    <div class="step"><div class="circ"><svg width="30" height="30" viewBox="0 0 24 24" fill="none" stroke="#4a2b1c" stroke-width="1.3"><path d="M4 21V9l8-5 8 5v12M8 21v-8M12 21v-8M16 21v-8"/></svg></div><div class="num">04</div><div class="lbl">Freeze Drying</div></div>
    <div class="step"><div class="circ"><svg width="30" height="30" viewBox="0 0 24 24" fill="none" stroke="#4a2b1c" stroke-width="1.3"><path d="M7 3h10v18H7zM7 7h10M10 12h4"/></svg></div><div class="num">05</div><div class="lbl">Packaging</div></div>
    <div class="step"><div class="circ"><svg width="30" height="30" viewBox="0 0 24 24" fill="none" stroke="#4a2b1c" stroke-width="1.3"><path d="M3 10l9-6 9 6v11H3zM8 21v-6h8v6"/></svg></div><div class="num">06</div><div class="lbl">Storage</div></div>
    <div class="step"><div class="circ"><svg width="30" height="30" viewBox="0 0 24 24" fill="none" stroke="#4a2b1c" stroke-width="1.3"><circle cx="12" cy="12" r="9"/><path d="M12 7l4 2.5v5L12 17l-4-2.5v-5z"/></svg></div><div class="num">07</div><div class="lbl">Distribution</div></div>
  </div>
</section>

<section class="caps">
  <h2 class="sec-title">CAPABILITIES</h2>
  <p class="sec-sub">We manage every stage in-house, allowing full control over quality, consistency, and speed to market.</p>
  <div class="cards">
    <div class="card"><div class="img" role="img" aria-label="Stainless packaging machinery on a production floor" style="background:linear-gradient(135deg,#5b6066,#aeb3b6 50%,#3f7f8a)"></div><h3>OEM / Private Label</h3><p>Custom manufacturing solutions built for scalable brands.</p><span class="go"><svg width="9" height="9" viewBox="0 0 10 10" fill="none" stroke="#231f1d" stroke-width="1.6"><path d="M2 5h6M5 2l3 3-3 3"/></svg></span></div>
    <div class="card"><div class="img" role="img" aria-label="Freeze-dried vegetables and fruit pieces" style="background:linear-gradient(135deg,#7fa54a,#e3823f 45%,#3e6b2b 80%)"></div><h3>Freeze Drying</h3><p>Advanced preservation technology for quality and shelf stability.</p><span class="go"><svg width="9" height="9" viewBox="0 0 10 10" fill="none" stroke="#231f1d" stroke-width="1.6"><path d="M2 5h6M5 2l3 3-3 3"/></svg></span></div>
    <div class="card"><div class="img" role="img" aria-label="Chef preparing dishes in a test kitchen" style="background:linear-gradient(135deg,#e9ecef,#9aa0a6 50%,#5a5f63)"></div><h3>R&amp;D Test Kitchen</h3><p>Product development, formulation, and innovation support.</p><span class="go"><svg width="9" height="9" viewBox="0 0 10 10" fill="none" stroke="#231f1d" stroke-width="1.6"><path d="M2 5h6M5 2l3 3-3 3"/></svg></span></div>
  </div>
</section>

<section class="why">
  <div class="abs ghost" aria-hidden="true">BRINDLE</div>
  <h2 class="abs">WHY BRINDLE</h2>
  <div class="ph why-halo"></div>
  <div class="ph why-circle" role="img" aria-label="Freeze-drying chamber with trays of yellow product"></div>
  <div class="ph why-person" role="img" aria-label="Team member in work apron presenting with open hands"></div>
  <div class="abs dot" style="left:708px;top:60px"></div>
  <div class="abs dot" style="left:752px;top:148px"></div>
  <div class="abs dot" style="left:758px;top:250px"></div>
  <div class="abs dot" style="left:724px;top:342px"></div>
  <div class="abs why-item" style="left:740px;top:20px"><span class="circ"><svg width="24" height="24" viewBox="0 0 24 24" fill="none" stroke="#fff" stroke-width="1.5"><path d="M3 21V10l5 3V10l5 3V6h5v15z"/></svg></span>Closed-loop Manufacturing</div>
  <div class="abs why-item" style="left:784px;top:108px"><span class="circ"><svg width="24" height="24" viewBox="0 0 24 24" fill="none" stroke="#fff" stroke-width="1.5"><circle cx="12" cy="12" r="8"/><path d="M8 12l3 3 5-6"/></svg></span>Integrated Quality Assurance</div>
  <div class="abs why-item" style="left:790px;top:210px"><span class="circ"><svg width="24" height="24" viewBox="0 0 24 24" fill="none" stroke="#fff" stroke-width="1.5"><circle cx="12" cy="12" r="8"/><path d="M12 7l4 2.5v5L12 17l-4-2.5v-5z"/></svg></span>Scalable Production</div>
  <div class="abs why-item" style="left:752px;top:302px"><span class="circ"><svg width="24" height="24" viewBox="0 0 24 24" fill="none" stroke="#fff" stroke-width="1.5"><path d="M6 3h9l3 3v15H6zM9 10h6M9 14h4"/></svg></span>Full Traceability</div>
</section>

<section class="cta">
  <div class="ph cta-halo"></div>
  <div class="ph cta-bag1" role="img" aria-label="Pouch of freeze-dried pet treats"></div>
  <div class="ph cta-bag2" role="img" aria-label="Pouch of freeze-dried vegetables"></div>
  <h2 class="abs">LET'S BUILD<br>SOMETHING TOGETHER</h2>
  <p class="abs">From concept to distribution, Brindle delivers integrated freeze-drying and manufacturing solutions tailored to your industry.</p>
  <span class="btn btn-brown">Start a Project <span class="arr"><svg width="9" height="9" viewBox="0 0 10 10" fill="none" stroke="#fff" stroke-width="1.6"><path d="M2 5h6M5 2l3 3-3 3"/></svg></span></span>
</section>

<footer class="foot">
  <div class="vline" style="left:360px"></div>
  <div class="vline" style="left:560px"></div>
  <div class="vline" style="left:720px"></div>
  <div class="vline" style="left:880px"></div>
  <div class="cols">
    <div class="col" style="width:250px">
      <div class="flogo">BRINDLE</div>
      <div style="color:#fff;font-size:11px;margin:2px 0 16px">Nutrition, Frozen in Time</div>
      <p style="width:190px">Brindle was built out of a problem that became impossible to ignore. During COVID, we saw how much high-quality food was going to waste. Farmers were left with surplus product and no efficient way to preserve or scale it.</p>
    </div>
    <div class="col" style="width:200px;padding-right:14px">
      <h4>CONTACT US</h4>
      <ul><li><span class="sic"></span><span class="txt">+1 555 014 2290</span></li><li><span class="sic"></span><span class="txt">sales@brindleharvest.example</span></li></ul>
    </div>
    <div class="col" style="width:160px;padding-left:20px">
      <h4>MAIN LINK</h4>
      <ul><li>Home</li><li>Pet Food</li><li>Agri-Food</li><li>Capabilities</li><li>Contact</li></ul>
    </div>
    <div class="col" style="width:160px;padding-left:20px">
      <h4>FOLLOW US</h4>
      <ul><li><span class="sic"></span>Photo Feed</li><li><span class="sic"></span>Updates</li><li><span class="sic"></span>Network</li></ul>
    </div>
    <div class="col" style="padding-left:20px">
      <h4>SUBSCRIBE NEWSLETTER</h4>
      <div class="email">Enter Your Email</div>
      <span class="btn btn-rust" style="margin-top:16px;width:160px;justify-content:space-between">Subscribe <span class="arr"><svg width="9" height="9" viewBox="0 0 10 10" fill="none" stroke="#fff" stroke-width="1.6"><path d="M2 5h6M5 2l3 3-3 3"/></svg></span></span>
    </div>
  </div>
  <div class="copyright">© 2026 Brindle — Nutrition, Frozen in Time. All Rights Reserved.</div>
</footer>

</body>
</html>
```